Buff & Gleam

polished concrete and epoxy coatings flooring company

Target Market(s)

Industrial commercial

Industry/Entity Type

Industrial flooring contractor

Contact Information for Business Card

POLISHED CONCRETE • EPOXY COATING • TERRAZZO RESTORATION • SHOT BLASTING • SURFACE PREPARATION • JOINT FILLING • TILE/ CARPET /GLUE REMOVAL

Colors
0054AA
0677BA
7BADD7
CADEEF
E8F1F8

Requirements
Must have
• email buffandgleamfloors@mailbrook.example Address 47215 Tallowmere Rd, Fraser, MI 48093. Name Ray Tulvin. Services Polished concrete- Epoxy Coatings- Terrazzo restoration-surface preparation- safety striping- joint filling- tile/ carpet/ glue removal phone number 586-700-3926 email buffandgleamfloors.example
Nice to have
• Instagram Facebook logo maybe smaller in the corner

```html
<!DOCTYPE html>
<html lang="en">
<head>
<meta charset="utf-8">
<title>Buff &amp; Gleam — Business Card</title>
<link href="https://fonts.googleapis.com/css2?family=EB+Garamond:wght@400;600&display=swap" rel="stylesheet">
<style>
  :root{
    --backdrop:#e4e6e9;
    --card-white:#ffffff;
    --ink:#111111;
    --ink-soft:#333333;
    --photo-dark:#3a2618;
    --photo-mid:#7a4a28;
    --photo-warm:#c98a4a;
    --photo-glow:#f2c27a;
    --photo-window:#4d5a3c;
    --on-photo:#ffffff;
    --icon-blue:#0677ba;
  }
  *{margin:0;padding:0;box-sizing:border-box}
  html,body{width:1200px;height:900px;overflow:hidden}
  body{background:var(--backdrop);position:relative;font-family:"EB Garamond",serif}

  .card{position:absolute;width:640px;height:366px;border-radius:4px;overflow:hidden;
        box-shadow:0 10px 28px rgba(0,0,0,.18)}
  .card--front{left:110px;top:60px}
  .card--back{left:450px;top:475px;background:var(--card-white)}

  .card__photo{position:absolute;inset:0;
    background:
      radial-gradient(ellipse at 32% 70%, var(--photo-glow) 0%, rgba(242,194,122,0) 40%),
      linear-gradient(180deg, var(--photo-window) 0%, #6b5a3a 38%, var(--photo-mid) 55%, var(--photo-warm) 72%, var(--photo-dark) 100%);}
  .card__shade{position:absolute;inset:0;background:linear-gradient(90deg,rgba(0,0,0,.05),rgba(0,0,0,.25))}

  .brand{position:absolute;right:32px;display:flex;align-items:center;gap:12px;
         font-family:"EB Garamond",serif;font-weight:600;font-size:40px;line-height:1;white-space:nowrap}
  .brand__mark{width:16px;height:16px;flex:none}
  .card--front .brand{top:150px;color:var(--on-photo)}
  .card--front .brand__mark{background:var(--on-photo)}
  .card--back .brand{top:56px;color:var(--ink)}
  .card--back .brand__mark{background:var(--ink)}

  .services{position:absolute;left:34px;bottom:34px;color:var(--on-photo);font-size:17px;line-height:1.45;list-style:none}
  .services__title{letter-spacing:1px;font-size:16px}
  .services li::before{content:"✦ ";font-size:11px;vertical-align:2px}
  .services .services__title::before{content:none}

  .contact{position:absolute;left:34px;bottom:28px;color:var(--ink-soft)}
  .contact__name{font-weight:600;font-size:19px;letter-spacing:1px;color:var(--ink);margin-bottom:8px}
  .contact__row{display:flex;align-items:center;gap:9px;font-size:16px;line-height:1.5}
  .contact__row svg{width:14px;height:14px;flex:none}
  .contact__divider{width:360px;height:1px;background:var(--ink-soft);margin:8px 0 6px}
  .contact__address{font-size:16px}
</style>
</head>
<body>

<section class="card card--front">
  <div class="card__photo" role="img" aria-label="Photo of a sunlit room with tall windows and a glossy polished floor reflecting the light"></div>
  <div class="card__shade"></div>
  <p class="brand"><span class="brand__mark"></span>Buff &amp; Gleam</p>
  <ul class="services">
    <li class="services__title">SERVICES -</li>
    <li>Polished Concrete ✦ Epoxy Coating</li>
    <li>Terrazzo Restoration ✦ Shot Blasting</li>
    <li>Surface Preparation ✦ Joint Filling</li>
    <li>Tile/ Carpet /glue Removal</li>
  </ul>
</section>

<section class="card card--back">
  <p class="brand"><span class="brand__mark"></span>Buff &amp; Gleam</p>
  <div class="contact">
    <p class="contact__name">RAY TULVIN</p>
    <p class="contact__row">
      <svg viewBox="0 0 16 16" aria-hidden="true"><path fill="var(--icon-blue)" d="M3.5 1l2.5 3-1.5 1.8c.9 2 2.6 3.8 4.7 4.7L11 9l3 2.5-1.5 2.8C7.5 14 2 8.5 1.7 3.5z"/></svg>
      586-700-3926</p>
    <p class="contact__row">
      <svg viewBox="0 0 16 16" aria-hidden="true"><rect x="1" y="3" width="14" height="10" fill="var(--icon-blue)"/><path d="M1 3l7 6 7-6" fill="none" stroke="#fff" stroke-width="1.3"/></svg>
      buffandgleamfloors@mailbrook.example</p>
    <p class="contact__row">
      <svg viewBox="0 0 16 16" aria-hidden="true"><g fill="none" stroke="var(--icon-blue)" stroke-width="1.3"><circle cx="8" cy="8" r="6.5"/><ellipse cx="8" cy="8" rx="3" ry="6.5"/><path d="M1.5 8h13M2.5 5h11M2.5 11h11"/></g></svg>
      buffandgleamfloors.example</p>
    <div class="contact__divider"></div>
    <p class="contact__address">47215 Tallowmere Rd, Fraser, MI 48093</p>
  </div>
</section>

</body>
</html>
```